Awesome design needed for standup comedy portal

We need a website designed for a new portal (pebblorx.com) dedicated to standup comedy.

- homepage
- featured "hero" content at top
- banner advertising
- browse comics
- browse venues
- search
- signup / login
- social media links

- comic page
- name
- pictures
- calendar of performances
- list of albums (with buy buttons)
- list of specials (Vodaloom, uCrate, etc. with buy buttons)
- reviews
- latest tweets
- latests photolyn photos
- links to social media accounts
- links to qvrt, podcast

- venue page
- name
- pictures
- address, phone number
- calendar of events
- reviews
- latest tweets
- links to qvrt, podcast

Target Market(s)

Fans of standup comedy and comedians

Number of Pages Required

3 page

Font styles to use
Sans Serif

Requirements
Must have
• Will eventually be implemented in bootstrap, so please keep that in mind

```html
<!DOCTYPE html>
<html lang="en">
<head>
<meta charset="utf-8">
<title>Pebblorx — Venue</title>
<link href="https://fonts.googleapis.com/css2?family=Open+Sans:wght@400;600;700&display=swap" rel="stylesheet">
<style>
:root{
  --red:#c0121a;
  --maroon:#7c1418;
  --ink:#333;
  --muted:#666;
  --line:#ddd;
  --tweet:#1d9bd8;
  --photo:#8a5a44;
  --gold:#c9b21c;
  --footer:#2b2b2b;
}
*{box-sizing:border-box;margin:0;padding:0}
html,body{width:1200px;height:2239px;overflow:hidden}
body{position:relative;font-family:"Open Sans",Arial,sans-serif;color:var(--ink);background:#fff}
.abs{position:absolute}
.site-header{position:absolute;left:0;top:0;width:1200px;height:169px;background:linear-gradient(#fafafa,#efefef)}
.social{left:76px;top:62px;display:flex;align-items:center;gap:14px;font-size:13px;font-weight:700;color:var(--maroon)}
.social i{width:17px;height:17px;border-radius:50%;background:#555;display:block}
.rule{left:76px;top:116px;width:440px;height:1px;background:#ccc}
.brand{left:540px;top:28px;width:120px;text-align:center}
.brand .dot{width:62px;height:62px;border-radius:50%;background:var(--red);margin:0 auto 6px}
.brand span{font-size:27px;font-weight:700;color:var(--red);letter-spacing:.5px}
.field{height:36px;border:1px solid #ccc;background:#fff;font-size:13px;color:#555;padding:9px 12px}
.search-btn{left:1088px;top:55px;width:37px;height:36px;background:var(--red)}
.nav a{position:absolute;top:134px;font-size:15px;font-weight:700;color:#333;text-decoration:none;letter-spacing:.3px}
.nav a.active{color:var(--red)}
.nav .underline{position:absolute;left:713px;top:163px;width:78px;height:4px;background:var(--red)}
.btn-signup{left:933px;top:124px;width:91px;height:37px;background:var(--maroon);color:#fff;font-size:13px;font-weight:700;text-align:center;line-height:37px}
.btn-login{left:1036px;top:124px;width:91px;height:37px;border:1px solid var(--red);background:#fff;color:#333;font-size:13px;font-weight:700;text-align:center;line-height:35px}
.section-title{font-size:24px;font-weight:700;color:var(--red);letter-spacing:.5px}
.body-text{font-size:14px;line-height:27.5px;color:#555}
.contact-row{display:flex;align-items:center;gap:18px;font-size:13px;color:#777}
.contact-row .ico{width:37px;height:37px;border-radius:50%;display:flex;align-items:center;justify-content:center}
.contact-row b{font-size:17px;color:#444;font-weight:700}
.divider{left:76px;width:1049px;height:2px;background:#e2e2e2}
.center-title{left:0;width:1200px;text-align:center;font-size:24px;font-weight:700;color:#444;letter-spacing:.5px}
.center-title em{font-style:normal;color:var(--red)}
.calendar{left:704px;top:707px;width:421px;height:324px;border:1px solid #e4e4e4;background:#fff}
.cal-head{height:53px;background:#f2f2f2;position:relative;text-align:center;line-height:53px;font-size:16px;font-weight:700;color:var(--red)}
.cal-arrow{position:absolute;top:0;width:28px;height:53px;background:var(--red);display:flex;align-items:center;justify-content:center}
.cal-days{position:absolute;left:26px;top:75px;display:grid;grid-template-columns:repeat(7,52.6px);font-size:11px;font-weight:700;color:#444;text-align:center}
.cal-grid{position:absolute;left:26px;top:100px;display:grid;grid-template-columns:repeat(7,52.6px);grid-auto-rows:39px;border-left:1px solid #ddd;border-top:1px solid #ddd}
.cal-grid div{border-right:1px solid #ddd;border-bottom:1px solid #ddd;font-size:12px;color:#555;display:flex;align-items:center;justify-content:center}
.cal-grid .today{background:var(--red);color:#fff}
.cal-grid .off{color:#ccc}
.pager{display:flex;gap:6px}
.pager svg{display:block}
.special-label{font-size:13px;font-weight:700;color:var(--red);letter-spacing:.3px;display:flex;align-items:center;gap:10px}
.special-label.dark{color:#333}
.special-text{font-size:14px;line-height:26px;color:#555;width:245px}
.buy{width:77px;height:35px;color:#fff;font-size:13px;font-weight:700;text-align:center;line-height:35px;border-radius:2px}
.review h4{font-size:12.5px;font-weight:700;color:var(--red);letter-spacing:.3px;margin-bottom:8px}
.review p{font-size:13px;line-height:25px;color:#555;width:495px}
.stars{display:flex;gap:2px;margin-top:6px}
.feed-title{font-size:24px;font-weight:700;display:flex;align-items:center;gap:10px;letter-spacing:.3px}
.insta-box{left:76px;top:1688px;width:506px;height:218px;border:2px solid #e3e3e3}
.thumbs{position:absolute;left:15px;top:13px;display:grid;grid-template-columns:repeat(5,83px);gap:17px 15px}
.thumbs div{height:83px;border-radius:3px}
.tweet h5{font-size:12.5px;font-weight:700;color:var(--tweet);display:flex;align-items:center;gap:6px;letter-spacing:.2px}
.tweet p{font-size:12.5px;line-height:25px;color:#555;width:530px;margin-top:4px}
.tweet a{color:var(--tweet);text-decoration:none}
.site-footer{left:0;top:2018px;width:1200px;height:221px;background:var(--footer);color:#bbb}
.f-brand{left:76px;top:1960px;width:140px;text-align:center}
.f-brand .dot{width:66px;height:66px;border-radius:50%;background:var(--red);margin:0 auto 4px}
.f-brand span{font-size:26px;font-weight:700;color:var(--red)}
.f-head{font-size:12.5px;font-weight:700;color:#fff;letter-spacing:.5px}
.f-text{font-size:12px;line-height:20px;color:#bbb}
.f-links a{position:absolute;font-size:13px;color:#ccc;text-decoration:none}
.f-icons{left:76px;top:2158px;display:flex;gap:12px;align-items:center}
.f-icons i{width:16px;height:16px;background:#666;display:block;border-radius:2px}
.f-icons span{font-size:15px;font-weight:700;color:#666}
.news-input{left:885px;top:2091px;width:240px;height:37px;background:#8a8a8a;color:#eee;font-size:13px;padding:9px 13px}
.news-btn{left:1037px;top:2142px;width:88px;height:34px;background:var(--red);color:#fff;font-size:13px;font-weight:700;text-align:center;line-height:34px}
.page-mark{right:10px;bottom:12px;font-size:13px;color:#fff}
</style>
</head>
<body>

<header class="site-header">
  <div class="abs social">SOCIAL: <i></i><i></i><i></i><i></i><i></i></div>
  <div class="abs rule"></div>
  <div class="abs brand"><div class="dot"></div><span>Pebblorx</span></div>
  <div class="abs field" style="left:713px;top:55px;width:178px">Browse Comics</div>
  <div class="abs field" style="left:900px;top:55px;width:178px">Browse Venues</div>
  <div class="abs search-btn">
    <svg width="37" height="36" viewBox="0 0 37 36"><circle cx="17" cy="16" r="6" fill="none" stroke="#fff" stroke-width="2.4"/><line x1="21.5" y1="20.5" x2="25.5" y2="24.5" stroke="#fff" stroke-width="2.6" stroke-linecap="round"/></svg>
  </div>
  <nav class="nav">
    <a style="left:96px">HOME</a>
    <a style="left:193px">ABOUT</a>
    <a style="left:296px">SERVICES</a>
    <a style="left:416px">COMICS</a>
    <a class="active" style="left:718px">VENUES</a>
    <a style="left:828px">CONTACT</a>
    <span class="underline"></span>
  </nav>
  <div class="abs btn-signup">SIGN UP</div>
  <div class="abs btn-login">LOG IN</div>
</header>

<h1 class="abs section-title" style="left:76px;top:222px">VENUE</h1>
<p class="abs body-text" style="left:76px;top:263px;width:670px">There are many variations of passages of Lorem Ipsum available, but the majority have suffered alteration in some form, by injected humour, or randomised words which don't look even slightly believable. If you are going to use a passage of Lorem Ipsum, you need to be sure there isn't anything embarrassing hidden in the middle of text. All the Lorem Ipsum generators on the Internet tend to repeat predefined chunks as necessary,.</p>
<div class="abs contact-row" style="left:75px;top:418px">
  <span class="ico" style="background:var(--red)"><svg width="16" height="16" viewBox="0 0 24 24"><path d="M6.6 10.8a15 15 0 0 0 6.6 6.6l2.2-2.2c.3-.3.7-.4 1-.2 1.1.4 2.3.6 3.6.6.6 0 1 .4 1 1V20c0 .6-.4 1-1 1A17 17 0 0 1 3 4c0-.6.4-1 1-1h3.5c.6 0 1 .4 1 1 0 1.3.2 2.5.6 3.6.1.3 0 .7-.2 1z" fill="#fff"/></svg></span>
  <span>Call us today &nbsp;<b>444-618-2907</b></span>
</div>
<div class="abs contact-row" style="left:75px;top:477px">
  <span class="ico" style="background:#333"><svg width="16" height="14" viewBox="0 0 16 14"><rect x="1" y="1.5" width="14" height="11" rx="1.5" fill="none" stroke="#fff" stroke-width="1.6"/><path d="M1.5 2.5 8 8l6.5-5.5" fill="none" stroke="#fff" stroke-width="1.6"/></svg></span>
  <span>Address : <b>no-25 setut perspiciatis unde omnis iste natus</b></span>
</div>
<div class="abs" role="img" aria-label="Ventriloquist on stage with a puppet under blue light" style="left:763px;top:227px;width:362px;height:285px;background:radial-gradient(circle at 65% 45%,#3a4c8a,#14204a 70%)"></div>

<div class="abs divider" style="top:571px"></div>

<h2 class="abs center-title" style="top:619px"><em>CALENDAR</em> OF EVENTS</h2>
<div class="abs" role="img" aria-label="Comedian performing with a puppet on a dark stage" style="left:76px;top:707px;width:591px;height:324px;background:radial-gradient(circle at 50% 50%,#3a3a3a,#111 70%)"></div>

<div class="abs calendar">
  <div class="cal-head">MARCH
    <span class="cal-arrow" style="left:0"><svg width="10" height="14"><path d="M8 2 3 7l5 5" fill="none" stroke="#fff" stroke-width="2.4"/></svg></span>
    <span class="cal-arrow" style="right:0"><svg width="10" height="14"><path d="M2 2l5 5-5 5" fill="none" stroke="#fff" stroke-width="2.4"/></svg></span>
  </div>
  <div class="cal-days"><span>Mon</span><span>Tue</span><span>Wed</span><span>Thu</span><span>Fri</span><span>Sat</span><span>Sun</span></div>
  <div class="cal-grid">
    <div>1</div><div>2</div><div>3</div><div>4</div><div>5</div><div>6</div><div>7</div>
    <div>8</div><div>9</div><div>10</div><div>11</div><div>12</div><div>13</div><div>14</div>
    <div>15</div><div>16</div><div>17</div><div>18</div><div>19</div><div>20</div><div>21</div>
    <div>22</div><div>23</div><div>24</div><div>25</div><div>26</div><div>27</div><div>28</div>
    <div>29</div><div class="today">30</div><div>31</div><div class="off">1</div><div class="off">2</div><div class="off">3</div><div class="off">4</div>
  </div>
</div>

<div class="abs divider" style="top:1077px"></div>

<h2 class="abs section-title" style="left:75px;top:1118px">SPECIALS</h2>
<div class="abs pager" style="left:538px;top:1126px">
  <svg width="19" height="19"><circle cx="9.5" cy="9.5" r="8" fill="none" stroke="#888" stroke-width="1.6"/><path d="M11 6 7.5 9.5 11 13" fill="none" stroke="#888" stroke-width="1.6"/></svg>
  <svg width="19" height="19"><circle cx="9.5" cy="9.5" r="8" fill="none" stroke="#888" stroke-width="1.6"/><path d="M8 6l3.5 3.5L8 13" fill="none" stroke="#888" stroke-width="1.6"/></svg>
</div>
<div class="abs" role="img" aria-label="Comedian holding a microphone against a blue backdrop" style="left:75px;top:1192px;width:241px;height:157px;background:linear-gradient(135deg,#3b8fc4,#1c5f91)"></div>
<div class="abs" role="img" aria-label="Ventriloquist performing with a puppet" style="left:343px;top:1192px;width:243px;height:157px;background:radial-gradient(circle at 60% 45%,#34468a,#141e48 70%)"></div>
<div class="abs special-label" style="left:75px;top:1376px"><span>VODALOOM</span><span>LOREM IPSUM DOLOR</span></div>
<div class="abs special-label dark" style="left:343px;top:1372px"><svg width="26" height="26"><circle cx="13" cy="13" r="12" fill="#2f6fb6"/></svg><span>LOREM IPSUM DOLOR</span></div>
<p class="abs special-text" style="left:75px;top:1397px">Sit amet consect- etuer adipiscing elit, sed diam nonummy orem euis- mod ultrices posuere cubilia....</p>
<p class="abs special-text" style="left:343px;top:1397px">Sit amet consect- etuer adipiscing elit, sed diam nonummy orem euis- mod ultrices posuere cubilia....</p>
<div class="abs buy" style="left:75px;top:1489px;background:var(--red)">BUY</div>
<div class="abs buy" style="left:343px;top:1489px;background:#3a3a3a">BUY</div>

<h2 class="abs section-title" style="left:629px;top:1118px">REVIEWS</h2>
<div class="abs pager" style="left:1076px;top:1126px">
  <svg width="19" height="19"><circle cx="9.5" cy="9.5" r="8" fill="none" stroke="#888" stroke-width="1.6"/><path d="M11 6 7.5 9.5 11 13" fill="none" stroke="#888" stroke-width="1.6"/></svg>
  <svg width="19" height="19"><circle cx="9.5" cy="9.5" r="8" fill="none" stroke="#888" stroke-width="1.6"/><path d="M8 6l3.5 3.5L8 13" fill="none" stroke="#888" stroke-width="1.6"/></svg>
</div>
<div class="abs review" style="left:630px;top:1188px">
  <h4>LOREM IPSUM DOLOR</h4>
  <p>Vestibulum vel metus sit amet turpis bibendum tincidunt vel sit amet quam metus sit amet turpis bibendum tincidunt vel sit amet quam.</p>
  <div class="stars"><svg width="70" height="12"><g fill="var(--gold)"><polygon points="6,0 7.5,4 12,4.3 8.5,7 9.7,11.5 6,9 2.3,11.5 3.5,7 0,4.3 4.5,4"/><polygon transform="translate(14)" points="6,0 7.5,4 12,4.3 8.5,7 9.7,11.5 6,9 2.3,11.5 3.5,7 0,4.3 4.5,4"/><polygon transform="translate(28)" points="6,0 7.5,4 12,4.3 8.5,7 9.7,11.5 6,9 2.3,11.5 3.5,7 0,4.3 4.5,4"/></g><g fill="#999"><polygon transform="translate(42)" points="6,0 7.5,4 12,4.3 8.5,7 9.7,11.5 6,9 2.3,11.5 3.5,7 0,4.3 4.5,4"/><polygon transform="translate(56)" points="6,0 7.5,4 12,4.3 8.5,7 9.7,11.5 6,9 2.3,11.5 3.5,7 0,4.3 4.5,4"/></g></svg></div>
</div>
<div class="abs review" style="left:630px;top:1310px">
  <h4>LOREM IPSUM DOLOR</h4>
  <p>Vestibulum vel metus sit amet turpis bibendum tincidunt vel sit amet quam metus sit amet turpis bibendum tincidunt vel sit amet quam.</p>
  <div class="stars"><svg width="70" height="12"><g fill="var(--gold)"><polygon points="6,0 7.5,4 12,4.3 8.5,7 9.7,11.5 6,9 2.3,11.5 3.5,7 0,4.3 4.5,4"/><polygon transform="translate(14)" points="6,0 7.5,4 12,4.3 8.5,7 9.7,11.5 6,9 2.3,11.5 3.5,7 0,4.3 4.5,4"/><polygon transform="translate(28)" points="6,0 7.5,4 12,4.3 8.5,7 9.7,11.5 6,9 2.3,11.5 3.5,7 0,4.3 4.5,4"/></g><g fill="#999"><polygon transform="translate(42)" points="6,0 7.5,4 12,4.3 8.5,7 9.7,11.5 6,9 2.3,11.5 3.5,7 0,4.3 4.5,4"/><polygon transform="translate(56)" points="6,0 7.5,4 12,4.3 8.5,7 9.7,11.5 6,9 2.3,11.5 3.5,7 0,4.3 4.5,4"/></g></svg></div>
</div>
<div class="abs review" style="left:630px;top:1432px">
  <h4>LOREM IPSUM DOLOR</h4>
  <p>Vestibulum vel metus sit amet turpis bibendum tincidunt vel sit amet quam metus sit amet turpis bibendum tincidunt vel sit amet quam.</p>
  <div class="stars"><svg width="70" height="12"><g fill="var(--gold)"><polygon points="6,0 7.5,4 12,4.3 8.5,7 9.7,11.5 6,9 2.3,11.5 3.5,7 0,4.3 4.5,4"/><polygon transform="translate(14)" points="6,0 7.5,4 12,4.3 8.5,7 9.7,11.5 6,9 2.3,11.5 3.5,7 0,4.3 4.5,4"/><polygon transform="translate(28)" points="6,0 7.5,4 12,4.3 8.5,7 9.7,11.5 6,9 2.3,11.5 3.5,7 0,4.3 4.5,4"/></g><g fill="#999"><polygon transform="translate(42)" points="6,0 7.5,4 12,4.3 8.5,7 9.7,11.5 6,9 2.3,11.5 3.5,7 0,4.3 4.5,4"/><polygon transform="translate(56)" points="6,0 7.5,4 12,4.3 8.5,7 9.7,11.5 6,9 2.3,11.5 3.5,7 0,4.3 4.5,4"/></g></svg></div>
</div>

<h2 class="abs feed-title" style="left:80px;top:1630px;color:var(--photo)"><svg width="26" height="26"><rect x="1" y="1" width="24" height="24" rx="3" fill="var(--photo)"/></svg>PHOTOLYN FEED</h2>
<div class="abs insta-box">
  <div class="thumbs" role="img" aria-label="Grid of recent performance photos">
    <div style="background:#5a2a4a"></div><div style="background:#3a2e28"></div><div style="background:#4a7aa0"></div><div style="background:#2a2422"></div><div style="background:#6a2a3a"></div>
    <div style="background:#4a2a4a"></div><div style="background:#2a2a48"></div><div style="background:#5a2436"></div><div style="background:#4a2030"></div><div style="background:#2e2a26"></div>
  </div>
</div>

<h2 class="abs feed-title" style="left:618px;top:1630px;color:var(--tweet)"><svg width="24" height="24"><circle cx="12" cy="12" r="11" fill="var(--tweet)"/></svg>LATEST TWEETS</h2>
<div class="abs tweet" style="left:619px;top:1684px">
  <h5><svg width="10" height="10"><circle cx="5" cy="5" r="4.5" fill="var(--tweet)"/></svg>LOREM IPSUM @TWIPSUM &nbsp;10 MAR 2017</h5>
  <p>Duis ultrices vestibulum lacus non luctus. Praesent aliquet, <a>justo ut</a> accumsan &nbsp;bibendum, <a>sem erat sagittis</a> nunc...</p>
</div>
<div class="abs tweet" style="left:619px;top:1780px">
  <h5><svg width="10" height="10"><circle cx="5" cy="5" r="4.5" fill="var(--tweet)"/></svg>LOREM IPSUM @TWIPSUM &nbsp;10 MAR 2017</h5>
  <p>Duis ultrices vestibulum lacus non luctus. Praesent bibendum, <a>sem erat</a> nunc...</p>
</div>
<div class="abs tweet" style="left:619px;top:1850px">
  <h5><svg width="10" height="10"><circle cx="5" cy="5" r="4.5" fill="var(--tweet)"/></svg>LOREM IPSUM @TWIPSUM &nbsp;10 MAR 2017</h5>
  <p>Duis ultrices vestibulum lacus non luctus. Praesent aliquet, <a>justo ut</a> accumsan bibendum, <a>sem erat sagittis</a> nunc...</p>
</div>

<footer class="abs site-footer">
  <p class="abs f-text" style="left:76px;top:83px;font-size:11.5px">Copyright © 2017. Company Name<br>All Right Reserved</p>
  <h3 class="abs f-head" style="left:357px;top:48px">QUICK LINKS</h3>
  <div class="f-links">
    <a style="left:357px;top:77px">Home</a><a style="left:457px;top:77px">Comics</a>
    <a style="left:357px;top:107px">About</a><a style="left:457px;top:107px">Venues</a>
    <a style="left:357px;top:137px">Services</a><a style="left:457px;top:137px">Contact</a>
  </div>
  <h3 class="abs f-head" style="left:615px;top:48px">CONTACT INFO</h3>
  <p class="abs f-text" style="left:615px;top:76px;font-size:13px">4120 Quillon<br>Road,Brackford, K17 3WT</p>
  <div class="abs f-text" style="left:615px;top:123px;font-size:13px;display:flex;gap:20px;align-items:center"><svg width="12" height="12" viewBox="0 0 24 24"><path d="M6.6 10.8a15 15 0 0 0 6.6 6.6l2.2-2.2c.3-.3.7-.4 1-.2 1.1.4 2.3.6 3.6.6.6 0 1 .4 1 1V20c0 .6-.4 1-1 1A17 17 0 0 1 3 4c0-.6.4-1 1-1h3.5c.6 0 1 .4 1 1 0 1.3.2 2.5.6 3.6.1.3 0 .7-.2 1z" fill="#bbb"/></svg>1-866-417-3092</div>
  <div class="abs f-text" style="left:615px;top:153px;font-size:13px;display:flex;gap:20px;align-items:center"><svg width="12" height="10" viewBox="0 0 16 14"><rect x="1" y="1.5" width="14" height="11" fill="#bbb"/><path d="M1.5 2.5 8 8l6.5-5.5" fill="none" stroke="#2b2b2b" stroke-width="1.6"/></svg>hello@pebblorx.com</div>
  <h3 class="abs f-head" style="left:885px;top:48px">NEWSLETTER SIGN UP</h3>
</footer>
<div class="abs f-brand"><div class="dot"></div><span>Pebblorx</span></div>
<div class="abs f-icons"><i></i><i></i><i></i><i></i><span>qvrt</span><svg width="18" height="16" viewBox="0 0 18 16"><path d="M2 11V9a7 7 0 0 1 14 0v2" fill="none" stroke="#666" stroke-width="2"/><rect x="1" y="9" width="4" height="6" rx="1" fill="#666"/><rect x="13" y="9" width="4" height="6" rx="1" fill="#666"/></svg></div>
<div class="abs news-input">Enter Email Address</div>
<div class="abs news-btn">SIGN UP</div>
<div class="abs page-mark">X10</div>

</body>
</html>
```